Tasteful instructions for employees/guests to wash hands

Need an aesthetic visualisation of steps to wash hands.
While we would like to convey the proper steps to wash hands we also don't want to treat our staff/guests like children, rather provide a quick reminder.
Suggested sizes
16″ × 24″
11″ × 14″
A simplified version of these steps:
- Wet your hands with clean, running water (warm or cold), turn off the tap, and apply soap.
- Lather your hands by rubbing them together with the soap. Lather the backs of your hands, between your fingers, and under your nails.
- Scrub your hands for at least 20 seconds.
- Rinse your hands well under clean, running water.
- Dry your hands using a clean towel or air dry them.
Look and feel
Each slider illustrates characteristics of the customer's brand and the style your logo design should communicate.

```html
<!DOCTYPE html>
<html lang="en">
<head>
<meta charset="utf-8">
<title>How to Wash Your Hand</title>
<link href="https://fonts.googleapis.com/css2?family=Raleway:wght@400;800&display=swap" rel="stylesheet">
<style>
  :root {
    --backdrop: #f7f7f7;
    --paper: #ffffff;
    --ink: #111111;
    --step-text: #333333;
    --art-tone: #e4e4e4;
    --shadow: rgba(0, 0, 0, 0.28);
  }
  html, body {
    margin: 0;
    padding: 0;
    width: 1200px;
    height: 728px;
    overflow: hidden;
    background: var(--backdrop);
  }
  .canvas {
    position: relative;
    width: 1200px;
    height: 728px;
  }
  .poster {
    position: absolute;
    left: 380px;
    top: 34px;
    width: 440px;
    height: 660px;
    background: var(--paper);
    box-shadow: 6px 6px 8px var(--shadow);
  }
  .poster-title {
    position: absolute;
    left: 0;
    right: 0;
    top: 18px;
    margin: 0;
    text-align: center;
    font-family: "Raleway", sans-serif;
    font-weight: 800;
    font-size: 24px;
    letter-spacing: 0.12em;
    color: var(--ink);
  }
  .step-art {
    position: absolute;
    left: 26px;
    width: 68px;
    background: var(--art-tone);
    border-radius: 4px;
  }
  .step-text {
    position: absolute;
    left: 108px;
    margin: 0;
    font-family: "Raleway", sans-serif;
    font-weight: 400;
    font-size: 8.6px;
    line-height: 10.4px;
    letter-spacing: 0.12em;
    color: var(--step-text);
  }
  .step-rule {
    position: absolute;
    left: 27px;
    width: 386px;
    height: 6px;
  }
</style>
</head>
<body>
<main class="canvas">
  <article class="poster">
    <h1 class="poster-title">HOW TO WASH YOUR HAND</h1>

    <div class="step-art" style="top:78px;height:75px" role="img" aria-label="Line drawing of hands under running water"></div>
    <p class="step-text" style="top:126px">Wet your hands with clean,<br>running water (warm or cold)</p>
    <svg class="step-rule" style="top:161px" viewBox="0 0 386 6" preserveAspectRatio="none"><path d="M0 3 Q193 1.5 386 3 Q193 4.5 0 3Z" fill="var(--ink)"/></svg>

    <div class="step-art" style="top:193px;height:42px" role="img" aria-label="Line drawing of soapy hands under a closed tap"></div>
    <p class="step-text" style="top:228px">Turn off the tap and apply soap</p>
    <svg class="step-rule" style="top:248px" viewBox="0 0 386 6" preserveAspectRatio="none"><path d="M0 3 Q193 1.5 386 3 Q193 4.5 0 3Z" fill="var(--ink)"/></svg>

    <div class="step-art" style="top:274px;height:52px" role="img" aria-label="Line drawing of hands rubbing together with lather"></div>
    <p class="step-text" style="top:301px">Lather your hands by rubbing them<br>together with the soap</p>
    <svg class="step-rule" style="top:335px" viewBox="0 0 386 6" preserveAspectRatio="none"><path d="M0 3 Q193 1.5 386 3 Q193 4.5 0 3Z" fill="var(--ink)"/></svg>

    <div class="step-art" style="top:365px;height:46px" role="img" aria-label="Line drawing of hands washing backs and between fingers"></div>
    <p class="step-text" style="top:381px">Lather the backs of your hands,<br>between your fingers and under your nails</p>
    <svg class="step-rule" style="top:417px" viewBox="0 0 386 6" preserveAspectRatio="none"><path d="M0 3 Q193 1.5 386 3 Q193 4.5 0 3Z" fill="var(--ink)"/></svg>

    <div class="step-art" style="top:451px;height:61px" role="img" aria-label="Line drawing of hands rinsed under running water"></div>
    <p class="step-text" style="top:484px">Rinse your hands well under clean,<br>running water</p>
    <svg class="step-rule" style="top:519px" viewBox="0 0 386 6" preserveAspectRatio="none"><path d="M0 3 Q193 1.5 386 3 Q193 4.5 0 3Z" fill="var(--ink)"/></svg>

    <div class="step-art" style="top:551px;height:78px" role="img" aria-label="Line drawing of hands drying on a towel"></div>
    <p class="step-text" style="top:601px">Dry your hands using a clean towel<br>or air dry them</p>
    <svg class="step-rule" style="top:638px" viewBox="0 0 386 6" preserveAspectRatio="none"><path d="M0 3 Q193 1.5 386 3 Q193 4.5 0 3Z" fill="var(--ink)"/></svg>
  </article>
</main>
</body>
</html>
```